The Amp Fellow

need a business card for a dj and sound equipment hire(rentals) business based in Melbourne. i have attached a current card get an idea. card needs to be unique professional looking.

ps.this card is not for a DJ. it's a rental business of dj equipment and pa systems.

Industry/Entity Type

Business

Font styles to use
Sans Serif
Script

Requirements
Must have
• Business Name: THE AMP FELLOW
Contact Person: RAVINDU PERERALA
Mobile: 047 BASSY 82
Email: RAVINDU@THEAMPFELLOW.COM.AU
Website: WWW.THEAMPFELLOW.COM.AU
Facebook: WWW.FANBOOTH.CM/THEAMPFELLOW.COM.AU

```html
<!DOCTYPE html>
<html lang="en">
<head>
<meta charset="utf-8">
<title>The Amp Fellow – Business Card</title>
<link rel="stylesheet" href="https://fonts.googleapis.com/css2?family=Orbitron:wght@900&family=Michroma&family=Open+Sans:wght@400;600&display=swap">
<style>
  :root {
    --page-bg: #f2f2f2;
    --card-bg: #070708;
    --gear-tone: #1b1c1f;
    --brand-blue: #2f6cc4;
    --spark-blue: #7fb3ff;
    --spark-core: #e6f0ff;
    --name-cream: #f3f0dc;
    --text-white: #f4f4f4;
  }
  * { margin: 0; padding: 0; box-sizing: border-box; }
  html, body {
    width: 1200px;
    height: 900px;
    overflow: hidden;
    background: var(--page-bg);
  }
  .business-card {
    position: absolute;
    left: 100px;
    top: 160px;
    width: 1000px;
    height: 580px;
    border-radius: 48px;
    background: var(--card-bg);
    overflow: hidden;
    color: var(--text-white);
    text-align: center;
  }
  .gear-backdrop {
    position: absolute;
    inset: 0;
    background:
      radial-gradient(circle at 50% 34%, #2a2b2f 0, #151619 22%, transparent 42%),
      radial-gradient(ellipse at 12% 60%, var(--gear-tone) 0, transparent 40%),
      radial-gradient(ellipse at 88% 62%, var(--gear-tone) 0, transparent 38%);
    opacity: 0.9;
  }
  .spark-line {
    position: absolute;
    left: 0;
    top: 212px;
    width: 100%;
    height: 40px;
    background: radial-gradient(ellipse at center, var(--spark-core) 0, var(--spark-blue) 8%, rgba(60,120,230,0.35) 30%, transparent 62%);
  }
  .spark-floor {
    position: absolute;
    left: 0;
    bottom: 0;
    width: 100%;
    height: 130px;
    background: linear-gradient(to top, rgba(120,170,255,0.55) 0, rgba(70,120,220,0.35) 35%, rgba(40,80,180,0.12) 70%, transparent 100%);
  }
  .card-text {
    position: absolute;
    left: 0;
    width: 100%;
    z-index: 1;
  }
  .contact-name {
    top: 72px;
    font-family: "Michroma", sans-serif;
    font-size: 21px;
    letter-spacing: 1px;
    color: var(--name-cream);
  }
  .brand-name {
    top: 196px;
    font-family: "Orbitron", sans-serif;
    font-weight: 900;
    font-size: 56px;
    line-height: 72px;
    letter-spacing: 2px;
    color: var(--brand-blue);
  }
  .tagline {
    top: 282px;
    font-family: "Michroma", sans-serif;
    font-size: 16px;
    letter-spacing: 1.5px;
    color: var(--text-white);
  }
  .contact-list {
    top: 372px;
    list-style: none;
    font-family: "Open Sans", sans-serif;
    font-size: 22px;
    line-height: 32px;
    letter-spacing: 0.5px;
  }
  .contact-list .phone {
    font-weight: 600;
    font-size: 26px;
    line-height: 38px;
    color: var(--brand-blue);
  }
</style>
</head>
<body>
  <article class="business-card">
    <div class="gear-backdrop" role="img" aria-label="Dark photo of a studio microphone and mixing desk"></div>
    <div class="spark-line" role="img" aria-label="Horizontal electric spark running across the card"></div>
    <div class="spark-floor" role="img" aria-label="Blue electric sound-wave sparks along the bottom edge"></div>

    <p class="card-text contact-name">RAVINDU PERERALA</p>
    <h1 class="card-text brand-name">THE AMP FELLOW</h1>
    <p class="card-text tagline">DJ AND SOUND EQUIPMENT HIRE</p>

    <ul class="card-text contact-list">
      <li class="phone">047 BASSY 82</li>
      <li>RAVINDU@THEAMPFELLOW.COM.AU</li>
      <li>WWW.THEAMPFELLOW.COM.AU</li>
      <li>WWW.FANBOOTH.CM/THEAMPFELLOW.COM.AU</li>
    </ul>
  </article>
</body>
</html>
```